Akademie für Gestaltung Lindenhof sucht Plakat-Design für Veranstaltung
Zielgruppe
Wird sind die Akademie für Gestaltung Lindenhof. Es handelt sich um die Veranstaltung 'Werkschau Abend'. Die Zielgruppe sind Personen, die sich für neue Technologien interessieren. Studenten präsentieren ihre Projekte die sie übers Semester erarbeitet haben.
Die Werkschau Abend findet am 31.01.2019 statt. Alle Informationen müssen ersichtlich auf dem Plakat sein
Akademie für Gestaltung Lindenhof
Kastanienweg. 7
70412 Stuttgart
Aufgabenstellung
Es soll schlich gehalten werden.

```html
<!DOCTYPE html>
<html lang="de">
<head>
<meta charset="utf-8">
<title>Werkschau Abend – Plakat</title>
<link rel="stylesheet" href="https://fonts.googleapis.com/css2?family=Electrolize&family=PT+Sans+Narrow&display=swap">
<style>
  :root {
    --stage: #1c1f21;
    --poster: #000000;
    --headline: #ffffff;
    --accent: #e2103c;
    --info: #ffffff;
    --muted: #8a8a8a;
  }
  html, body {
    margin: 0;
    padding: 0;
    width: 1200px;
    height: 2786px;
    overflow: hidden;
    background: var(--stage);
  }
  .canvas {
    position: relative;
    width: 1200px;
    height: 2786px;
  }
  .poster {
    position: absolute;
    left: 0;
    top: 544px;
    width: 1200px;
    height: 1698px;
    display: block;
  }
  .poster-bg { fill: var(--poster); }
  .headline {
    font-family: "Electrolize", sans-serif;
    font-size: 184px;
    fill: var(--headline);
  }
  .date {
    font-family: "Electrolize", sans-serif;
    font-size: 70px;
    fill: var(--accent);
  }
  .info {
    font-family: "PT Sans Narrow", sans-serif;
    font-size: 32px;
    fill: var(--info);
  }
  .institution-mark { fill: var(--accent); }
  .institution-name {
    font-family: "PT Sans Narrow", sans-serif;
    font-size: 25px;
    fill: var(--muted);
  }
</style>
</head>
<body>
<div class="canvas">
  <svg class="poster" viewBox="0 0 1200 1698" xmlns="http://www.w3.org/2000/svg" aria-labelledby="poster-title">
    <title id="poster-title">Werkschau Abend, 31.01.2019, Akademie für Gestaltung Lindenhof</title>
    <rect class="poster-bg" x="0" y="0" width="1200" height="1698"/>

    <text class="headline" transform="translate(603 1407) rotate(-90)" textLength="1165" lengthAdjust="spacingAndGlyphs">Werkschau Abend</text>
    <text class="date" transform="translate(672 427) rotate(-90)" textLength="380" lengthAdjust="spacingAndGlyphs">31.01.2019</text>

    <g class="event-details">
      <text class="info" x="767" y="1344">Werkschau Abend</text>
      <text class="info" x="767" y="1389">31. Januar 2018</text>
      <text class="info" x="767" y="1434">ab 18 Uhr</text>
    </g>

    <g class="venue-address">
      <text class="info" x="767" y="1522">Akademie für Gestaltung Lindenhof</text>
      <text class="info" x="767" y="1567">Kastanienweg 7</text>
      <text class="info" x="767" y="1612">70412 Stuttgart</text>
    </g>

    <g class="institution">
      <rect class="institution-mark" x="467" y="1497" width="40" height="40"/>
      <text class="institution-name" x="467" y="1572">AKADEMIE FÜR</text>
      <text class="institution-name" x="467" y="1600">GESTALTUNG</text>
      <text class="institution-name" x="467" y="1628">LINDENHOF</text>
    </g>
  </svg>
</div>
</body>
</html>
```